Book Cover - For Best Selling Diet

Hi
Book cover required for a diet book being marketed to become a best seller
For best quality, image will be 2820 pixels on the shortest side and 4500 pixels on the longest side .
The book name : Bright Morning Plan
By Corinna Plett
( will add in the extra text once we see design - top and bottom subtitle )
I do not want a photo of a person on the book.
PLEASE SEE " THE 9 STEP FRAME" by Ned Galbury as an example of solid style and I also love Quiet Ledger for the font.
Branding Colours:
#F26432
#A4195C
#A7D8CC
Font that runs through our brand is : helvetica neue
This is for a book that will be marketed for #1 bestseller - So please only quality
designs that are designed in a unique style.
Thanks
Target Market(s)
Busy Working Mums, Affluent, 30+ .
Look and feel

```html
<!DOCTYPE html>
<html lang="en">
<head>
<meta charset="utf-8">
<title>Bright Morning Plan – Book Cover</title>
<link rel="stylesheet" href="https://fonts.googleapis.com/css2?family=Bebas+Neue&family=Oswald:wght@400;500&family=Crimson+Text:wght@400;700&display=swap">
<style>
  :root {
    --purple: #8568a6;
    --purple-dark: #6b4f8c;
    --teal: #7fcfc0;
    --pink: #e0448e;
    --white: #ffffff;
    --sky: #a9d6ec;
  }
  html, body {
    margin: 0;
    padding: 0;
    width: 1200px;
    height: 861px;
    overflow: hidden;
    background: var(--purple);
  }
  .cover {
    position: relative;
    width: 1200px;
    height: 861px;
    background: var(--purple);
    overflow: hidden;
    font-family: "Crimson Text", Georgia, serif;
    color: var(--white);
  }
  .back-copy {
    position: absolute;
    left: 17px;
    top: 8px;
    width: 300px;
    font-size: 14.2px;
    line-height: 17.6px;
    text-align: justify;
    margin: 0;
  }
  .back-copy p { margin: 0 0 18px; }

  .author-box {
    position: absolute;
    left: 14px;
    top: 422px;
    width: 296px;
    height: 439px;
    background: var(--pink);
    padding: 16px 12px 0 14px;
    box-sizing: border-box;
  }
  .author-box__name {
    font-family: "Oswald", "Arial Narrow", sans-serif;
    font-weight: 400;
    font-size: 25px;
    line-height: 30px;
    margin: 0;
  }
  .author-box__label {
    font-weight: 700;
    font-size: 16px;
    letter-spacing: 1.4px;
    margin: 2px 0 6px;
  }
  .author-box__bio {
    font-size: 14.2px;
    line-height: 17.6px;
    text-align: justify;
    margin: 0 0 18px;
  }

  .web-address {
    position: absolute;
    left: 356px;
    top: 699px;
    font-family: "Oswald", "Arial Narrow", sans-serif;
    font-size: 20px;
    color: var(--teal);
    margin: 0;
  }
  .isbn-box {
    position: absolute;
    left: 346px;
    top: 728px;
    width: 206px;
    height: 124px;
    background: var(--white);
    color: #000;
    font-size: 38px;
    display: flex;
    align-items: center;
    justify-content: center;
  }

  .spine {
    position: absolute;
    left: 558px;
    top: 0;
    width: 83px;
    height: 861px;
    background: var(--teal);
  }
  .spine__emblem {
    position: absolute;
    left: 8px;
    top: 16px;
    width: 66px;
    height: 32px;
    background: var(--purple);
    border-radius: 16px;
  }

  .front-subtitle {
    position: absolute;
    left: 720px;
    top: 360px;
    width: 404px;
    font-size: 15.5px;
    line-height: 19px;
    text-align: center;
    margin: 0;
  }
  .front-figure {
    position: absolute;
    left: 838px;
    top: 402px;
    width: 146px;
    height: 344px;
    border-radius: 60px 60px 10px 10px;
    background: linear-gradient(180deg, #e65aa0, var(--pink));
  }
  .front-author {
    position: absolute;
    left: 700px;
    top: 742px;
    width: 426px;
    text-align: center;
    font-family: "Oswald", "Arial Narrow", sans-serif;
    font-weight: 500;
    font-size: 44px;
    line-height: 54px;
    color: var(--teal);
    margin: 0;
  }
  .front-rule {
    position: absolute;
    left: 700px;
    top: 805px;
    width: 426px;
    height: 1px;
    background: var(--teal);
    opacity: 0.6;
  }
  .front-blurb {
    position: absolute;
    left: 700px;
    top: 814px;
    width: 426px;
    font-size: 13.5px;
    line-height: 17px;
    text-align: center;
    color: var(--sky);
    margin: 0;
  }

  .type-layer {
    position: absolute;
    left: 0;
    top: 0;
    width: 1200px;
    height: 861px;
    pointer-events: none;
  }
  .display { font-family: "Bebas Neue", "Oswald", sans-serif; fill: var(--teal); }
  .spine-title { font-family: "Bebas Neue", "Oswald", sans-serif; fill: var(--purple); }
  .spine-author { font-family: "Oswald", "Arial Narrow", sans-serif; font-weight: 500; fill: var(--purple-dark); }
</style>
</head>
<body>
<div class="cover">

  <!-- Back cover -->
  <div class="back-copy">
    <p>Vivamus at lacus sit amet tortor viverra egestas id sed turpis. Nulla tincidunt ante vel suscipit interdum. In sed consectetur purus. Phasellus porttitor erat vitae massa euismod porta. Proin pulvinar urna cursus imperdiet gravida. Maecenas ut facilisis ipsum. Phasellus vehicula tempor varius. In suscipit consequat nunc, ut facilisis arcu vulputate sed. Aliquam cursus ante felis, eget rhoncus diam lacinia quis. Sed vitae magna id mi tempor rutrum. In et leo at metus ultricies lobortis.</p>
    <p>Donec vitae erat molestie, gravida velit eget, lacinia leo. Vivamus ac erat augue. Curabitur quis turpis id purus ultricies consequat ac eu nibh. Aenean tincidunt, libero a condimentum posuere, lectus odio aliquam ligula, at aliquet nulla libero et massa. Integer non augue id nibh porta</p>
  </div>

  <div class="author-box">
    <h3 class="author-box__name">Corinna Plett</h3>
    <div class="author-box__label">ABOUT THE AUTHOR</div>
    <p class="author-box__bio">Adipiscing. Aenean ac nibh in odio dapibus cursus a et turpis. Curabitur sagittis in arcu eget vestibulum. Suspendisse condimentum pellentesque leo, sodales vestibulum diam tincidunt placerat. Aliquam ultricies arcu eu ipsum posuere, vel dignissim justo gravida. Duis ullamcorper, nibh in semper sodales, risus quam egestas tortor, et gravida dui sem quis elit. Sed nec tristique erat.</p>
    <p class="author-box__bio">Nulla facilisi. Curabitur dignissim, enim ultrices scelerisque rhoncus, elit arcu varius diam, non tristique libero libero convallis urna. Integer sed sem sed arcu viverra sollicitudin. Cum sociis natoque penatibus et magnis dis parturient</p>
  </div>

  <p class="web-address">www.cplettbooks.com</p>
  <div class="isbn-box">ISBN</div>

  <!-- Spine -->
  <div class="spine">
    <div class="spine__emblem" role="img" aria-label="Small running woman figure"></div>
  </div>

  <!-- Front cover -->
  <p class="front-subtitle">Vivamus at lacus sit amet tortor viverra egestas id sed turpis. Nulla tincidunt ante vel suscipit.</p>
  <div class="front-figure" role="img" aria-label="Pink silhouette of a woman walking in heels"></div>
  <h2 class="front-author">Corinna Plett</h2>
  <div class="front-rule"></div>
  <p class="front-blurb">Donec vitae erat molestie, gravida velit eget, lacinia leo. Vivamus ac erat augue. Curabitur quis turpis id purus ultricies consequat ac eu</p>

  <!-- Display type -->
  <svg class="type-layer" width="1200" height="861" viewBox="0 0 1200 861" aria-label="Bright Morning Plan">
    <text class="display" x="330" y="63" font-size="60" textLength="198" lengthAdjust="spacingAndGlyphs">BRIGHT MORNING</text>
    <text class="display" x="330" y="176" font-size="161" textLength="198" lengthAdjust="spacingAndGlyphs">PLAN</text>

    <g transform="translate(576,56) rotate(90)">
      <text class="spine-title" x="0" y="0" font-size="68" textLength="606" lengthAdjust="spacingAndGlyphs">BRIGHT MORNING PLAN</text>
    </g>
    <g transform="translate(585,697) rotate(90)">
      <text class="spine-author" x="0" y="0" font-size="32" textLength="148" lengthAdjust="spacingAndGlyphs">Corinna Plett</text>
    </g>

    <text class="display" x="701" y="134" font-size="120" textLength="426" lengthAdjust="spacingAndGlyphs">BRIGHT MORNING</text>
    <text class="display" x="701" y="352" font-size="311" textLength="426" lengthAdjust="spacingAndGlyphs">PLAN</text>
  </svg>

</div>
</body>
</html>
```